Irrigation Business needs their business cards modernised and revamped

I would like to keep my current logo, colours and revamp the format of the card.

I would like the card to be clean yet important.

Im not sure if you include texture but i would like the named logo to be indented into the card etc.

show me something alive and free something thats clinical to the point yet has a feel of achievement. i would like people to go nice card.

Target Market(s)

high end clients, corporate, sports field manger, the guys that make the decisions

Industry/Entity Type

Business

Contact Information for Business Card

nformation to be included

Dorian Hesk (Director)
0487253916
dorian@tfcraft.biz
www.taddsfieldcrafts.com

instagram logo
google logo
facebook logo

Colors

Designer to choose colors to be used in the design.

Requirements
Nice to have
• indentations a really nice feel to the card good texture

```html
<!DOCTYPE html>
<html lang="en">
<head>
<meta charset="utf-8">
<title>Tadds Field Crafts – Business Card</title>
<link rel="stylesheet" href="https://fonts.googleapis.com/css2?family=Cabin:wght@400;500;700&display=swap">
<style>
  :root {
    --stage: #2c2c2c;
    --paper: #f1f1f0;
    --brand-blue: #3d6aa8;
    --logo-blue: #2f63a8;
    --accent-cyan: #3a9fd0;
    --accent-green: #2e9e54;
    --ink: #2a2a2a;
    --faint-on-paper: rgba(0, 0, 0, 0.06);
    --faint-on-blue: rgba(0, 0, 0, 0.07);
  }
  * { box-sizing: border-box; margin: 0; padding: 0; }
  html, body {
    width: 1200px; height: 600px; overflow: hidden;
    background: var(--stage);
    font-family: "Cabin", "Helvetica Neue", Arial, sans-serif;
  }
  .stage { position: relative; width: 1200px; height: 600px; }

  .card {
    position: absolute; top: 175px;
    width: 519px; height: 295px;
    overflow: hidden;
  }
  .card--front { left: 85px; background: var(--paper); }
  .card--back { left: 617px; background: var(--brand-blue); }

  .backdrop-circle {
    position: absolute; border-radius: 50%;
  }
  .card--front .backdrop-circle {
    left: 363px; top: -23px; width: 322px; height: 322px;
    background: var(--faint-on-paper);
  }
  .card--back .backdrop-circle {
    left: -160px; top: -20px; width: 320px; height: 320px;
    background: var(--faint-on-blue);
  }

  /* Front: identity */
  .identity { position: absolute; left: 16px; top: 15px; height: 45px; padding-left: 15px; }
  .identity::before {
    content: ""; position: absolute; left: 0; top: 0;
    width: 11px; height: 45px; background: var(--accent-cyan);
  }
  .identity__name { font-size: 21px; font-weight: 400; color: var(--ink); line-height: 1; padding-top: 9px; }
  .identity__role { font-size: 13px; color: var(--accent-green); line-height: 1.1; }

  /* Front: brand */
  .brand-front {
    position: absolute; right: 16px; top: 16px;
    display: flex; flex-direction: column; align-items: center; width: 190px;
  }
  .brand-front__dot {
    width: 64px; height: 64px; border-radius: 50%; background: var(--accent-cyan);
    border: 3px solid var(--logo-blue);
  }
  .brand-front__name {
    margin-top: 10px; font-weight: 700; font-size: 20px; line-height: 1.05;
    color: var(--logo-blue); text-align: center; letter-spacing: 0.5px;
  }

  /* Front: contact */
  .contact { position: absolute; left: 16px; top: 204px; list-style: none; }
  .contact__item {
    display: flex; align-items: center; gap: 8px;
    font-size: 15px; color: var(--ink); height: 25px;
  }
  .contact__icon { width: 15px; height: 12px; flex: none; }

  .rule {
    position: absolute; left: 0; top: 258px; width: 387px; height: 2px;
    background: var(--accent-cyan);
  }
  .website {
    position: absolute; left: 16px; top: 264px;
    font-size: 14px; color: var(--logo-blue);
  }
  .social {
    position: absolute; left: 405px; top: 250px;
    display: flex; gap: 21px; list-style: none;
  }
  .social__chip { width: 15px; height: 15px; background: var(--logo-blue); border-radius: 2px; }

  /* Back: brand */
  .brand-back {
    position: absolute; left: 0; right: 0; top: 53px;
    display: flex; flex-direction: column; align-items: center;
  }
  .brand-back__dot {
    width: 116px; height: 116px; border-radius: 50%;
    background: #ececec; border: 4px solid #ffffff;
  }
  .brand-back__name {
    margin-top: 20px; font-weight: 700; font-size: 33px; line-height: 1.1;
    color: #ececec; text-align: center; letter-spacing: 0.5px;
  }
</style>
</head>
<body>
<main class="stage">

  <section class="card card--front" aria-label="Card front">
    <div class="backdrop-circle" aria-hidden="true"></div>

    <header class="identity">
      <h1 class="identity__name">Dorian Hesk</h1>
      <p class="identity__role">Director</p>
    </header>

    <div class="brand-front">
      <span class="brand-front__dot" aria-hidden="true"></span>
      <p class="brand-front__name">TADDS FIELD CRAFTS</p>
    </div>

    <ul class="contact">
      <li class="contact__item">
        <svg class="contact__icon" viewBox="0 0 15 12" aria-hidden="true">
          <path d="M1 4 Q7.5 -1 14 4 L12 5.5 L10 4 L10 3 Q7.5 2 5 3 L5 4 L3 5.5 Z" fill="var(--accent-green)"/>
          <rect x="3" y="6" width="9" height="5" rx="1" fill="var(--accent-green)"/>
        </svg>
        0487253916
      </li>
      <li class="contact__item">
        <svg class="contact__icon" viewBox="0 0 15 12" aria-hidden="true">
          <rect x="0.5" y="1" width="14" height="10" fill="var(--accent-green)"/>
          <path d="M0.5 1 L7.5 7 L14.5 1" fill="none" stroke="var(--paper)" stroke-width="1.2"/>
        </svg>
        dorian@tfcraft.biz
      </li>
    </ul>

    <div class="rule" aria-hidden="true"></div>
    <p class="website">www.taddsfieldcrafts.com</p>

    <ul class="social" aria-label="Social profiles">
      <li class="social__chip" aria-label="Social profile"></li>
      <li class="social__chip" aria-label="Social profile"></li>
      <li class="social__chip" aria-label="Social profile"></li>
    </ul>
  </section>

  <section class="card card--back" aria-label="Card back">
    <div class="backdrop-circle" aria-hidden="true"></div>
    <div class="brand-back">
      <span class="brand-back__dot" aria-hidden="true"></span>
      <p class="brand-back__name">TADDS FIELD CRAFTS</p>
    </div>
  </section>

</main>
</body>
</html>
```